Stationary Design needed for Physical Therapy and Wellness Center

Letterhead, Envelopes, Business Cards (x2) needed. We are a studio specializing in helping our clients improve mobility, fitness, and recover from injury. We use the Velantric method and need to adhere to their trademark restrictions.
Updates

Target Market(s)

Potential Clients: active people...many from dance or athletic backgrounds.

Industry/Entity Type

Health And Wellness

Font styles to use
Sans Serif
Other font styles liked:
• Times New Roman for the word Velantric.

Colors
00a990
33b8a4
86cfc6
0393ce
33a6d7
85cae6

Requirements
Must have
• Attention to Velantric trademark guidelines (Times New Roman font, Bold type, use of registered trademark symbol). Examples of current stationary can be provided as an example.
• Concept of movement, flow.

```html
<!DOCTYPE html>
<html lang="en">
<head>
<meta charset="utf-8">
<title>Kinetica Studio – Envelope Stationery</title>
<link rel="stylesheet" href="https://fonts.googleapis.com/css2?family=Montserrat:wght@400&family=Tinos:wght@700&display=swap">
<style>
  :root {
    --backdrop: #e0f8f0;
    --paper: #ffffff;
    --paper-back: #ececec;
    --teal: #1fb8a6;
    --teal-deep: #00a990;
    --teal-soft: #5ccdc0;
    --ink-dark: #2e2e2e;
    --watermark: #eeeeee;
    --crease: #dcdcdc;
  }
  * { box-sizing: border-box; margin: 0; padding: 0; }
  html, body {
    width: 1200px; height: 950px; overflow: hidden;
    background: var(--backdrop);
    font-family: "Montserrat", sans-serif;
  }
  .canvas { position: relative; width: 1200px; height: 950px; }

  /* Envelope front */
  .envelope-front {
    position: absolute; left: 70px; top: 60px;
    width: 760px; height: 370px;
    background: var(--paper);
    box-shadow: 0 6px 18px rgba(0,0,0,0.12);
  }
  .envelope-front .sender {
    position: absolute; left: 36px; top: 40px;
  }
  .brand {
    display: flex; align-items: center; gap: 10px;
    color: var(--teal-deep); font-size: 30px; font-weight: 400;
    letter-spacing: 0.5px;
  }
  .brand-dot {
    width: 22px; height: 22px; border-radius: 50%;
    background: var(--teal-deep);
  }
  .sender-address {
    margin-top: 8px; margin-left: 32px;
    font-family: "Tinos", serif; font-weight: 700;
    font-size: 11px; line-height: 1.35; color: var(--teal-deep);
  }
  .front-watermark {
    position: absolute; right: 70px; top: 140px;
    width: 110px; height: 110px; border-radius: 50%;
    background: var(--watermark);
  }
  .front-edge {
    position: absolute; left: 0; right: 0; bottom: 0; height: 8px;
    background: var(--teal);
  }
  .front-edge-break {
    position: absolute; left: 260px; bottom: 0;
    width: 240px; height: 8px; background: var(--ink-dark);
  }

  /* Envelope back */
  .envelope-back {
    position: absolute; left: 370px; top: 490px;
    width: 770px; height: 390px;
    box-shadow: 0 6px 18px rgba(0,0,0,0.12);
  }
  .envelope-back svg { display: block; }
  .back-brand {
    position: absolute; left: 470px; top: 250px;
    font-size: 24px;
  }
  .back-brand .brand-dot { width: 18px; height: 18px; }
</style>
</head>
<body>
<main class="canvas">

  <section class="envelope-front" aria-label="Envelope front">
    <div class="sender">
      <div class="brand"><span class="brand-dot"></span><span>Kinetica Studio</span></div>
      <p class="sender-address">4120 Linden Avenue, Fairmont Hills,<br>Ohio 44021</p>
    </div>
    <div class="front-watermark" aria-hidden="true"></div>
    <div class="front-edge"></div>
    <div class="front-edge-break"></div>
  </section>

  <section class="envelope-back" aria-label="Envelope back">
    <svg width="770" height="390" viewBox="0 0 770 390">
      <defs>
        <linearGradient id="flapTone" x1="0" y1="0" x2="0" y2="1">
          <stop offset="0" stop-color="#45c7b8"/>
          <stop offset="1" stop-color="#22b8a7"/>
        </linearGradient>
      </defs>
      <rect class="back-paper" x="0" y="0" width="770" height="390" fill="var(--paper-back)"/>
      <path class="side-fold" d="M0 40 Q 330 200 0 380" fill="none" stroke="var(--crease)" stroke-width="1.5"/>
      <path class="side-fold" d="M770 40 Q 440 200 770 380" fill="none" stroke="var(--crease)" stroke-width="1.5"/>
      <path class="flap-lining" role="img" aria-label="Teal patterned flap lining"
            d="M0 16 Q0 0 16 0 L754 0 Q770 0 770 16 L770 70 Q 600 70 420 120 L 40 120 Q 0 120 0 100 Z"
            fill="url(#flapTone)"/>
    </svg>
    <div class="brand back-brand"><span class="brand-dot"></span><span>Kinetica Studio</span></div>
  </section>

</main>
</body>
</html>
```